Yoga and Wellness Center

New business- have the logo already, but wanted my cards to be more colorful.

Please find my attached logo. I am only waiting on confirmation of my
telephone number in order to have all the information right. This is for a
new yoga and wellness center in TN for a conservative audience, but I would
like a colorful business card.

Industry/Entity Type

Conservative

```html
<!DOCTYPE html>
<html lang="en">
<head>
<meta charset="utf-8">
<title>Stillwater Yoga – Business Card</title>
<link rel="stylesheet" href="https://fonts.googleapis.com/css2?family=Exo+2:wght@400;500;600&display=swap">
<style>
  :root {
    --navy: #24347f;
    --orange: #f2661f;
    --white: #ffffff;
    --ink: #2d2d33;
    --backdrop: #e9e7e3;
  }
  * { margin: 0; padding: 0; box-sizing: border-box; }
  html, body {
    width: 1200px; height: 901px; overflow: hidden;
    background: var(--backdrop);
    font-family: "Exo 2", sans-serif;
  }
  .card {
    position: absolute; left: 120px; top: 176px;
    width: 960px; height: 548px;
    border-radius: 48px; overflow: hidden;
    background: var(--white);
    box-shadow: 0 10px 30px rgba(0,0,0,.12);
  }
  .card__waves { position: absolute; inset: 0; width: 100%; height: 100%; }
  .brand {
    position: absolute; left: 150px; top: 120px;
    display: flex; align-items: center; gap: 16px;
  }
  .brand__dot {
    width: 58px; height: 58px; border-radius: 50%;
    background: var(--orange);
  }
  .brand__name {
    color: var(--navy); font-weight: 500; font-size: 30px;
    letter-spacing: 5px; text-transform: uppercase;
  }
  .person { position: absolute; left: 120px; top: 248px; }
  .person__name {
    color: var(--ink); font-weight: 500; font-size: 40px;
    letter-spacing: 1px; text-transform: uppercase; line-height: 1;
  }
  .person__role {
    margin-top: 10px; margin-left: 14px;
    color: var(--navy); font-weight: 500; font-size: 26px;
  }
  .contact {
    position: absolute; right: 72px; top: 318px;
    color: var(--white); text-align: right;
    font-size: 21px; line-height: 1.25; letter-spacing: .5px;
  }
  .contact__address { margin-bottom: 14px; }
  .contact__row {
    display: flex; justify-content: flex-end; align-items: center;
    gap: 10px; height: 30px;
  }
  .contact__row--web { font-size: 19px; }
  .contact__icon { width: 18px; height: 18px; fill: var(--white); flex: none; }
</style>
</head>
<body>
  <div class="card">
    <svg class="card__waves" viewBox="0 0 960 548" preserveAspectRatio="none" aria-hidden="true">
      <path fill="#f2661f" d="M0 292 C140 372 290 440 470 452 C300 470 140 425 0 376 Z"/>
      <path fill="#24347f" d="M0 362 C150 420 300 468 450 456 C560 440 680 230 960 190 L960 548 L0 548 Z"/>
      <path fill="none" stroke="#ffffff" stroke-width="4" d="M490 450 C595 428 700 240 960 202"/>
    </svg>

    <div class="brand">
      <span class="brand__dot"></span>
      <span class="brand__name">Stillwater Yoga</span>
    </div>

    <div class="person">
      <div class="person__name">Daniel Whitmore</div>
      <div class="person__role">Managing Director</div>
    </div>

    <div class="contact">
      <div class="contact__address">214 Maple Hollow Rd<br>Suite 3</div>
      <div class="contact__row">615 555 0142
        <svg class="contact__icon" viewBox="0 0 24 24"><path d="M6.6 10.8a15 15 0 0 0 6.6 6.6l2.2-2.2c.3-.3.7-.4 1-.2 1.1.4 2.3.6 3.6.6.6 0 1 .4 1 1V20c0 .6-.4 1-1 1A17 17 0 0 1 3 4c0-.6.4-1 1-1h3.5c.6 0 1 .4 1 1 0 1.3.2 2.5.6 3.6.1.3 0 .7-.2 1z"/></svg>
      </div>
      <div class="contact__row">615 555 0143
        <svg class="contact__icon" viewBox="0 0 24 24"><path d="M7 1h10a2 2 0 0 1 2 2v18a2 2 0 0 1-2 2H7a2 2 0 0 1-2-2V3a2 2 0 0 1 2-2zm0 3v14h10V4zm5 15.5a1 1 0 1 0 0 2 1 1 0 0 0 0-2z"/></svg>
      </div>
      <div class="contact__row">615 555 0144
        <svg class="contact__icon" viewBox="0 0 24 24"><path d="M6 2h9l3 3v5h2a2 2 0 0 1 2 2v8a2 2 0 0 1-2 2H4a2 2 0 0 1-2-2v-8a2 2 0 0 1 2-2h2zm2 2v6h8V6h-2V4zm-2 10v2h2v-2zm4 0v2h2v-2zm4 0v2h2v-2z"/></svg>
      </div>
      <div class="contact__row">hello@stillwater.com
        <svg class="contact__icon" viewBox="0 0 24 24"><path d="M2 5h20v14H2zm2 2v.5l8 5 8-5V7zm0 2.8V17h16V9.8l-8 5z"/></svg>
      </div>
      <div class="contact__row contact__row--web">www.stillwateryoga.com
        <svg class="contact__icon" viewBox="0 0 24 24"><path d="M12 2a10 10 0 1 0 0 20 10 10 0 0 0 0-20zm6.9 6h-3a15 15 0 0 0-1.3-3.9A8 8 0 0 1 18.9 8zM12 4c.8 1.2 1.5 2.5 1.9 4h-3.8c.4-1.5 1.1-2.8 1.9-4zM4.3 14a8 8 0 0 1 0-4h3.4a16 16 0 0 0 0 4zm.8 2h3a15 15 0 0 0 1.3 3.9A8 8 0 0 1 5.1 16zm3-8h-3a8 8 0 0 1 4.3-3.9C8.8 5.3 8.4 6.6 8.1 8zM12 20c-.8-1.2-1.5-2.5-1.9-4h3.8c-.4 1.5-1.1 2.8-1.9 4zm2.3-6H9.7a14 14 0 0 1 0-4h4.6a14 14 0 0 1 0 4zm.3 5.9c.6-1.2 1-2.5 1.3-3.9h3a8 8 0 0 1-4.3 3.9zM16.3 14a16 16 0 0 0 0-4h3.4a8 8 0 0 1 0 4z"/></svg>
      </div>
    </div>
  </div>
</body>
</html>
```